Business Card Design

Non-profit organization creating opportunities for:
Personal empowerment
Community Outreach
Healthier Life Choices
Body/Mind/Spirit Nourishment
Emotional Transformation
Charity & Network Opportunities
Everyday people making An extrodinary sufferance
All achieved from the Source within YOU.
Organization logo is the ying yang symbol with a small circle above it as if it were the head and the ying yang symbol was the body.  Also in side upper ying needs to be a heart and in the lower yang needs to be the letter C. This is very important as it came to me in a dream n the forming of this organization.  Color choice is open although a thought I hade was that the heart is red metallic foil (sine a red heart is the symbol of love)and the c is gold foil( the gifts of the 3 wise men and gold being one of them).a verticle card is preferred and logo as large as possible on it even if ying yang is made oval Ilook forward to the layouts and designs you can come up with.

Industry/Entity Type
Business
Contact Information for Business Card
Lumina Harbor. Org
Peter Galvany
Executive Director
Lumina harbor.peter@mailbrook.net
315-482-9063

```html
<!DOCTYPE html>
<html lang="en">
<head>
<meta charset="utf-8">
<title>Lumina Harbor. Org — Business Card</title>
<link href="https://fonts.googleapis.com/css2?family=Lato:wght@300;400;700&display=swap" rel="stylesheet">
<style>
  :root {
    --backdrop: #a9a9a9;
    --card: #f1f1f0;
    --ink: #2b2b2b;
    --accent-red: #d52a2f;
    --shadow: rgba(0, 0, 0, 0.28);
  }
  * { margin: 0; padding: 0; box-sizing: border-box; }
  html, body {
    width: 1200px;
    height: 747px;
    overflow: hidden;
    background: var(--backdrop);
    font-family: "Lato", sans-serif;
    color: var(--ink);
  }
  .stage {
    position: relative;
    width: 1200px;
    height: 747px;
    display: flex;
    justify-content: center;
    align-items: center;
    gap: 70px;
  }
  .card {
    width: 370px;
    height: 646px;
    background: var(--card);
    box-shadow: 0 6px 18px var(--shadow);
    position: relative;
  }

  /* Front */
  .card--front { display: flex; flex-direction: column; align-items: center; }
  .brand-mark {
    margin-top: 92px;
    display: flex;
    align-items: center;
    gap: 10px;
  }
  .brand-mark__dot {
    width: 22px;
    height: 22px;
    border-radius: 50%;
    background: var(--ink);
  }
  .brand-mark__name {
    font-size: 20px;
    font-weight: 700;
    color: var(--ink);
    letter-spacing: 0.02em;
  }
  .holder { margin-top: 172px; text-align: center; }
  .holder__name {
    font-size: 27px;
    font-weight: 700;
    letter-spacing: 0.08em;
    text-transform: uppercase;
    line-height: 1.1;
  }
  .holder__title {
    font-size: 25px;
    font-weight: 300;
    line-height: 1.2;
  }
  .divider {
    width: 220px;
    height: 2px;
    background: var(--accent-red);
    margin-top: 42px;
  }
  .contact { margin-top: 40px; text-align: center; font-size: 21px; line-height: 1.45; }
  .contact__org { font-weight: 700; }
  .contact__phone, .contact__email { font-weight: 400; }

  /* Back */
  .card--back {
    display: flex;
    flex-direction: column;
    align-items: center;
    justify-content: center;
    gap: 26px;
  }
  .emblem-circle {
    width: 230px;
    height: 230px;
    border-radius: 50%;
    background: var(--ink);
  }
  .emblem-name {
    font-size: 30px;
    font-weight: 700;
    color: var(--ink);
    letter-spacing: 0.02em;
  }
</style>
</head>
<body>
  <main class="stage">
    <section class="card card--front" aria-label="Card front">
      <div class="brand-mark">
        <span class="brand-mark__dot"></span>
        <span class="brand-mark__name">Lumina Harbor</span>
      </div>
      <div class="holder">
        <p class="holder__name">Peter Galvany</p>
        <p class="holder__title">Executive Director</p>
      </div>
      <div class="divider"></div>
      <div class="contact">
        <p class="contact__org">Lumina Harbor. Org</p>
        <p class="contact__phone">315-482-9063</p>
        <p class="contact__email">Lumina harbor.peter@mailbrook.net</p>
      </div>
    </section>

    <section class="card card--back" aria-label="Card back">
      <div class="emblem-circle"></div>
      <p class="emblem-name">Lumina Harbor</p>
    </section>
  </main>
</body>
</html>
```